Hair Extension Aftercare sheet

This sheet is to give to customers regarding the aftercare of hair extensions. There should be Simple and minimal look - approx A5 size and can be folded to suit. I have attached the content and logo files for use.
We are not looking for to much artwork just clean, professional look.
All the content provided in a compact flyer format i.e
A foldable A5 pamphlet or the like, this is for packaging requirements
Please do not submit A4 layouts

Industry/Entity Type

Hair And Beauty

Requirements
Must have
• All the content provided in a compact flyer format i.e
• A foldable A5 pamphlet or the like, this is for packaging requirements
Should not have
• tacky art work or images - must be clean lines

```html
<!DOCTYPE html>
<html lang="en">
<head>
<meta charset="utf-8">
<title>Marina Holt Hair Extensions – Aftercare and Maintenance Guidelines</title>
<link href="https://fonts.googleapis.com/css2?family=Open+Sans:ital,wght@0,400;0,700;1,400;1,700&display=swap" rel="stylesheet">
<style>
  :root {
    --brand-tan: #b89968;
    --accent-red: #c8102e;
    --footer-red: #a3141f;
    --ink: #1d1d1b;
    --paper: #ffffff;
  }
  * { margin: 0; padding: 0; box-sizing: border-box; }
  html, body { width: 843px; height: 1200px; overflow: hidden; background: var(--paper); }
  body { font-family: "Open Sans", Arial, sans-serif; color: var(--ink); }

  .sheet { position: relative; width: 843px; height: 1200px; }

  .brand { position: absolute; top: 38px; left: 0; width: 843px; text-align: center; color: var(--brand-tan); font-size: 30px; font-weight: 400; line-height: 40px; }

  .sheet-title { position: absolute; top: 96px; left: 28px; font-size: 15px; font-weight: 400; letter-spacing: 0.2px; }

  .column { position: absolute; top: 124px; width: 384px; font-size: 13.2px; line-height: 20px; }
  .column-left { left: 28px; }
  .column-right { left: 434px; }

  .column p { margin-bottom: 9px; }
  .column h2 { font-size: 13.2px; font-weight: 700; font-style: italic; margin-bottom: 8px; }
  .column p + h2 { margin-top: 14px; }
  .lead-in { font-weight: 700; font-style: italic; }
  .warning-title { color: var(--accent-red); }
  .warning { color: var(--accent-red); font-weight: 700; font-style: italic; }
  .warning-caps { color: var(--accent-red); font-weight: 700; text-transform: uppercase; }

  .footer-bar { position: absolute; left: 0; top: 1130px; width: 420px; height: 46px; background: var(--footer-red); }
  .footer-url { position: absolute; left: 20px; top: 6px; font-size: 24px; font-weight: 700; color: var(--paper); }
  .footer-page { position: absolute; right: 24px; top: 1142px; font-size: 18px; }
</style>
</head>
<body>
<main class="sheet">
  <header class="brand">Marina Holt Hair Extensions</header>

  <h1 class="sheet-title">AFTERCARE AND MAINTENANCE GUIDELINES</h1>

  <section class="column column-left">
    <p>It is very important to keep this exceptional quality hair in the best condition you can. Please read all of the information below:</p>
    <p>It is important to use the right tools for the job. A good hair brush is a small investment to keep your hair in the best possible condition and contributes to a pleasant wearing experience.</p>
    <p><span class="lead-in">Marina Holt Bristle Brushes</span> with small plastic pins and real bristle hair are ideal and specially developed for this purpose. It smooths the hair without loosing brushing grip and removes tangles effortlessly.</p>

    <h2>General:</h2>
    <p>Do not use oil based products, always use water dissolvable products. Oil based products will keep the hair in a wet condition and can cause matting. Oil based products attract a lot more dust and dirt which will make the hair less smooth and feel dry.</p>

    <h2>General Washing &amp; Conditioning:</h2>
    <p>Shampoo at least two times per week. Never wash, brush or dry the hair upside down. Before washing, brush out all tangles with a hair extension brush (available from Marina Holt Hair Extensions). Do not use a brush with only plastic or steel pins. Always start brushing or combing at the ends, working your way up to the roots.</p>
    <p>Wet the hair thoroughly, then disperse a small amount of shampoo into your hand and rub your hands together. Apply the shampoo evenly on the scalp and at the roots. Gently wash the scalp using your fingertips without rubbing the hair. Rinse thoroughly while squeezing the hair to remove all shampoo residue. If the shampoo does not foam the first time, don't apply more shampoo but continue washing as normal. After rinsing simply re-apply the shampoo for a second time. There is no need to apply a lot of shampoo in the lengths. The hair will get cleaned when you rinse the hair out (unless extremely dirty).</p>
    <p class="warning">Avoid: Shampoos that contain sulphates &amp; products that are oil based.</p>
    <p>If you can't wash it off your hands without shampoo, it is more likely oil based.</p>
  </section>

  <section class="column column-right">
    <h2>After you washed the hair:</h2>
    <p>After washing you may use a conditioner however, apply the conditioner from the ends to half way up the length. Never at the roots. Comb the conditioner through using a large wide tooth comb until all tangles are removed. Rinse thoroughly to leave no residue in the hair. Towel dry the hair by squeezing it with the towel. Don't rub or massage the hair.</p>
    <p>You can apply small amounts of leave-in conditioner or a recommended styling product, comb through with your fingers into the direction you would like your hair to fall and scrunch it upwards once more. After you have done this leave the hair to dry completely without touching, combing or brushing it. = Best natural result.</p>
    <p>Let it dry naturally or use your favourite styling equipment. Use leave in conditioners only at the ends! When the hair is completely dry.</p>

    <h2>At Night</h2>
    <p>Braid the hair in a large loose braid at the nape of the neck before going to sleep. Do not sleep with wet hair, this will cause tangling and will make it difficult to style the following morning.</p>

    <h2>Styling the hair</h2>
    <p>You can use a ceramic straightening iron or a hair dryer with a bristle brush to smooth the hair. Other styling tools that can be used are: Heated rollers, steam rollers, curling irons, hot air curling tongs and setting rollers.</p>

    <h2 class="warning-title">IMPORTANT:</h2>
    <p class="warning-caps">Never use hot styling equipment that exceeds 200 degrees Celsius or 392 degrees Fahrenheit.</p>
    <p>Temperatures above this can damage the protein in the hair causing it to solidify and make the hair dry and unmanageable. Always keep hot styling equipment moving through the hair and do not hold for too long in one place. We do not recommend using straightening irons on wet hair.</p>

    <h2>Sports and other activities</h2>
    <p>Don't expose your hair to strong windy conditions like sailing, motor sports, cabriolet cars. Wear protective head wear. If you sweat a lot during work outs, at least rinse out the saltiness as this will dry out the hair.</p>
  </section>

  <footer>
    <div class="footer-bar"><span class="footer-url">www.marinaholt.com</span></div>
    <span class="footer-page">(1)</span>
  </footer>
</main>
</body>
</html>
```